Clinician Supply Circle

I am a financial planner whose client's are physicians and dentists. As physicians, there is very little time for them to do research on numerous aspects of their business and personal lives. I am looking to build a website that is a 1 stop shop for many of the services/resources they may need. It will be my job to screen the resources/advertisers and place competent people/business's that I know and have a track record on. there will ultimately be 10 or 12 ish areas that I would like to provide resources in:
disability insurance
life insurance
retirement planning
student loan advisors
employment contract and business formation attorneys
accountants
real estate agents
physician mortgages
personal loans
malpractice insurance
physician recruiters
maybe 2 other areas which I have yet to figure out.....
I would like each of these options to be able to be clicked on and a page will open up with the 1 or 2 or 3 or 4 people/business's that I have picked to represent these areas. I would like each specific person/business to have a click here to contact me link in which an email goes to the person and I am copied on the initial correspondence between the physician and the mortgage broker.... just so I can see some of the correspondence they will be receiving.
nowhere on the site do I want it to say my name. there will be certain disclosures that are needed and other wording but I think this is a good starting point.
here are links to two websites with the same general concept. please keep in mind that I want my website to be more on the simple side.
http://www.quillbarrowpartners.example/index.html
http://fernlakeledger.example/
Updates
Industry/Entity Type
Financial

```html
<!DOCTYPE html>
<html lang="en">
<head>
<meta charset="utf-8">
<title>Clinician Supply Circle</title>
<link href="https://fonts.googleapis.com/css2?family=Dosis:wght@400;500;600;700&display=swap" rel="stylesheet">
<style>
:root{
  --blue:#35acd8;
  --blue-light:#6cc8e8;
  --blue-dark:#1f8fbc;
  --ink:#3a3a3a;
  --muted:#8a8a8a;
  --bar:#2d2d2d;
  --panel:#f1f1f1;
  --line:#d9d9d9;
  --white:#ffffff;
}
*{box-sizing:border-box;margin:0;padding:0}
html,body{width:673px;height:1200px;overflow:hidden;background:var(--white)}
body{font-family:"Dosis",sans-serif;color:var(--ink)}
.page{width:673px;height:1200px;position:relative;overflow:hidden}

.topbar{height:22px;background:var(--bar);display:flex;align-items:center;padding:0 40px;font-size:8px;color:#cfcfcf;gap:8px}
.topbar .dot{width:10px;height:10px;border-radius:50%;background:#555}
.topbar .spacer{flex:1}
.topbar .item{display:flex;align-items:center;gap:4px}

.header{height:42px;display:flex;align-items:center;padding:0 40px;border-bottom:1px solid #eee}
.brand{font-size:16px;font-weight:500;color:var(--ink);flex:1}
.nav{display:flex;gap:4px;font-size:9px}
.nav a{padding:5px 10px;color:var(--ink);text-decoration:none}
.nav a.active{background:var(--blue);color:var(--white)}

.hero{height:196px;background:linear-gradient(90deg,var(--blue-light),var(--blue));position:relative}
.hero-copy{position:absolute;left:42px;top:50px;color:var(--white)}
.hero-copy h1{font-size:21px;font-weight:600;letter-spacing:.3px}
.hero-copy p{font-size:10px;font-weight:600;margin-top:4px;color:#1e4f66}
.hero-btn{display:inline-flex;align-items:center;gap:8px;margin-top:16px;background:var(--bar);color:var(--white);font-size:8px;padding:6px 10px}
.hero-btn span.circle{width:11px;height:11px;border:1px solid var(--white);border-radius:50%;display:flex;align-items:center;justify-content:center}
.hero-photo{position:absolute;right:110px;top:0;width:170px;height:196px;background:linear-gradient(180deg,#eaf4f8,#c9dfe8)}
.hero-dots{position:absolute;left:50%;bottom:10px;display:flex;gap:4px;transform:translateX(-50%)}
.hero-dots i{width:5px;height:5px;border-radius:50%;background:rgba(255,255,255,.6)}
.hero-dots i:first-child{background:var(--white)}

.welcome{text-align:center;padding-top:18px;height:98px}
.welcome h2{font-size:19px;font-weight:500;line-height:1.1;letter-spacing:.5px}
.welcome .rule{width:40px;height:2px;background:var(--blue);margin:6px auto}
.welcome p{font-size:8px;color:var(--muted);letter-spacing:.5px}

.categories{display:grid;grid-template-columns:repeat(4,112px);column-gap:12px;row-gap:12px;justify-content:center}
.tile{height:160px;border-bottom:2px solid var(--blue)}
.tile-photo{height:110px;background:linear-gradient(135deg,#cfdbe3,#8fa6b4)}
.tile h3{font-size:8px;font-weight:700;margin-top:6px;letter-spacing:.3px}
.tile p{font-size:6.5px;color:var(--muted);margin-top:3px;line-height:1.35}

.features{position:absolute;left:0;top:875px;width:673px;height:115px;background:var(--panel);display:flex;justify-content:center;gap:40px;padding-top:16px}
.feature{width:125px;text-align:center}
.feature svg{display:block;margin:0 auto}
.feature h4{font-size:11px;font-weight:600;margin-top:6px}
.feature p{font-size:6.5px;color:var(--muted);margin-top:3px;line-height:1.35}
.feature .rule{height:2px;background:var(--blue);margin-top:6px}

.contact{position:absolute;left:42px;top:1005px;width:589px;display:flex;gap:34px}
.contact-form{width:280px}
.contact h5{font-size:11px;font-weight:600}
.contact .rule{width:100%;height:1px;background:var(--line);margin:4px 0 8px}
.form-grid{display:grid;grid-template-columns:1fr 1fr;gap:6px}
.fields{display:flex;flex-direction:column;gap:6px}
.field{height:18px;border:1px solid var(--line);font-size:6px;color:var(--muted);padding:5px}
.field.message{height:66px}
.send{margin-left:auto;margin-top:8px;width:60px;height:18px;background:var(--blue);color:var(--white);font-size:7px;display:flex;align-items:center;justify-content:center}
.info{flex:1;position:relative}
.info p{font-size:6.5px;color:var(--muted);line-height:1.4}
.info .social-title{margin-top:10px}
.socials{display:flex;gap:5px;margin-top:4px}
.socials i{width:12px;height:12px;border-radius:50%;background:var(--blue)}
.socials i:nth-child(2){background:#4b6aa8}
.socials i:nth-child(3){background:#d9534f}
.keep{font-size:11px;font-weight:600;margin-top:8px}
.location{position:absolute;right:0;top:40px;width:56px;height:58px;background:var(--bar);color:var(--white);font-size:7px;display:flex;flex-direction:column;align-items:center;justify-content:center;gap:4px}

.footer{position:absolute;left:0;bottom:0;width:673px;height:34px;background:var(--bar);display:flex;align-items:center;justify-content:space-between;padding:0 42px;color:#bdbdbd;font-size:7px}
.footer .mark{font-size:11px;color:#9a9a9a}
</style>
</head>
<body>
<div class="page">
  <div class="topbar">
    <span class="dot"></span><span class="dot"></span>
    <span class="item">Log In</span><span class="item">Sign Up</span>
    <span class="spacer"></span>
    <span class="item">
      <svg width="8" height="8" viewBox="0 0 10 10"><path d="M2 1l2 2-1 1.5c.6 1.2 1.3 1.9 2.5 2.5L7 6l2 2-1.2 1.2C4.5 9 1 5.5.8 2.2z" fill="#cfcfcf"/></svg>
      0800-555-0142</span>
    <span class="item">
      <svg width="9" height="7" viewBox="0 0 10 8"><rect x=".5" y=".5" width="9" height="7" fill="none" stroke="#cfcfcf"/><path d="M.5.5 5 4.5 9.5.5" fill="none" stroke="#cfcfcf"/></svg>
      hello@cliniciansupplycircle.example</span>
  </div>

  <header class="header">
    <div class="brand">Clinician Supply Circle</div>
    <nav class="nav">
      <a class="active">Home</a><a>About</a><a>Services</a><a>Blog</a><a>Contact</a>
    </nav>
  </header>

  <section class="hero">
    <div class="hero-copy">
      <h1>INSURANCE FOR PHYSICIANS !</h1>
      <p>EMPOWER PHYSICIANS TO PROTECT THEIR INCOME!</p>
      <div class="hero-btn">GET STARTED NOW <span class="circle">
        <svg width="5" height="5" viewBox="0 0 6 6"><path d="M1 3h4M3 1l2 2-2 2" stroke="#fff" fill="none"/></svg></span></div>
    </div>
    <div class="hero-photo" role="img" aria-label="Photo of a doctor in a white coat holding a tablet"></div>
    <div class="hero-dots"><i></i><i></i><i></i></div>
  </section>

  <section class="welcome">
    <h2>WELCOME TO THE<br>CLINICIAN SUPPLY CIRCLE</h2>
    <div class="rule"></div>
    <p>CATEGORIES, CHOOSE YOUR OPTION !</p>
  </section>

  <section class="categories">
    <div class="tile"><div class="tile-photo" role="img" aria-label="Photo of a patient in a wheelchair with a carer"></div><h3>DISABILITY INSURANCE</h3><p>Protect your income if illness stops you practicing.</p></div>
    <div class="tile"><div class="tile-photo" role="img" aria-label="Photo of doctors talking in a hospital"></div><h3>LIFE INSURANCE</h3><p>Term and whole policies to secure your family.</p></div>
    <div class="tile"><div class="tile-photo" role="img" aria-label="Photo of a retired couple meeting an advisor"></div><h3>RETIREMENT PLANNING</h3><p>Plan early and build savings that last longer.</p></div>
    <div class="tile"><div class="tile-photo" role="img" aria-label="Photo of graduates in caps and gowns"></div><h3>STUDENT LOAN ADVISORS</h3><p>Advisors who map the fastest path to payoff.</p></div>
    <div class="tile"><div class="tile-photo" role="img" aria-label="Photo of attorneys in a business meeting"></div><h3>BUSINESS ATTORNEYS</h3><p>Counsel for contracts, entities and partnership agreements today.</p></div>
    <div class="tile"><div class="tile-photo" role="img" aria-label="Photo of a recruitment meeting at a table"></div><h3>PHYSICIAN RECRUITERS</h3><p>Recruiters who match you with the right practice.</p></div>
    <div class="tile"><div class="tile-photo" role="img" aria-label="Photo of a medical team in scrubs"></div><h3>MALPRACTICE INSURANCE</h3><p>Liability cover chosen for your specialty and state.</p></div>
    <div class="tile"><div class="tile-photo" role="img" aria-label="Photo of a cheerful borrower"></div><h3>PERSONAL LOANS</h3><p>Fair rates for personal borrowing needs and plans.</p></div>
    <div class="tile"><div class="tile-photo" role="img" aria-label="Photo of a contract signing handshake"></div><h3>EMPLOYMENT CONTRACT</h3><p>Review terms before you sign your next offer.</p></div>
    <div class="tile"><div class="tile-photo" role="img" aria-label="Photo of accountants reviewing documents"></div><h3>ACCOUNTANTS</h3><p>Tax and bookkeeping help built for medical practices.</p></div>
    <div class="tile"><div class="tile-photo" role="img" aria-label="Photo of a real estate agent with clients"></div><h3>REAL ESTATE AGENTS</h3><p>Agents who know busy schedules and new towns.</p></div>
    <div class="tile"><div class="tile-photo" role="img" aria-label="Photo of a physician discussing a mortgage"></div><h3>PHYSICIAN MORTGAGES</h3><p>Home loans designed for residents and new physicians.</p></div>
  </section>

  <section class="features">
    <div class="feature">
      <svg width="34" height="34" viewBox="0 0 34 34"><path d="M17 3 29 8v9c0 7-5 12-12 14C10 29 5 24 5 17V8z" fill="var(--blue)"/><path d="M12 17l4 4 7-8" stroke="#fff" stroke-width="2.5" fill="none"/></svg>
      <h4>INSURANCE</h4><p>Screened advisors for every policy a doctor needs.</p><div class="rule"></div>
    </div>
    <div class="feature">
      <svg width="34" height="34" viewBox="0 0 34 34"><rect x="5" y="22" width="5" height="8" fill="var(--blue)"/><rect x="12" y="17" width="5" height="13" fill="var(--blue)"/><rect x="19" y="12" width="5" height="18" fill="var(--blue)"/><rect x="26" y="7" width="5" height="23" fill="var(--blue)"/><path d="M4 18 12 11l5 4 12-11" stroke="var(--blue)" stroke-width="2" fill="none"/></svg>
      <h4>FINANCIAL</h4><p>Trusted planners, accountants and lenders in one place.</p><div class="rule"></div>
    </div>
    <div class="feature">
      <svg width="34" height="34" viewBox="0 0 34 34"><circle cx="17" cy="17" r="14" fill="none" stroke="var(--blue)" stroke-width="3"/><circle cx="17" cy="17" r="8" fill="none" stroke="var(--blue)" stroke-width="3"/><circle cx="17" cy="17" r="3" fill="var(--blue)"/></svg>
      <h4>PLANNING</h4><p>Clear steps toward retirement, family and practice goals.</p><div class="rule"></div>
    </div>
  </section>

  <section class="contact">
    <div class="contact-form">
      <h5>CONTACT US</h5><div class="rule"></div>
      <div class="form-grid">
        <div class="fields">
          <div class="field">NAME</div>
          <div class="field">EMAIL</div>
          <div class="field">PHONE NO</div>
        </div>
        <div class="field message">MESSAGE</div>
      </div>
      <div class="send">SEND</div>
    </div>
    <div class="info">
      <h5>INFORMATION</h5><div class="rule"></div>
      <p style="width:140px">We screen every resource listed here so physicians and dentists can find trusted help quickly. Reach out with questions about any category.</p>
      <h5 class="social-title">SOCIAL</h5>
      <div class="socials"><i></i><i></i><i></i><i></i></div>
      <div class="keep">KEEP IN TOUCH</div>
      <div class="location">
        <svg width="14" height="18" viewBox="0 0 14 18"><path d="M7 1a6 6 0 0 0-6 6c0 4.5 6 10 6 10s6-5.5 6-10a6 6 0 0 0-6-6z" fill="#fff"/><circle cx="7" cy="7" r="2.2" fill="var(--bar)"/></svg>
        LOCATION
      </div>
    </div>
  </section>

  <footer class="footer">
    <span>Clinician Supply Circle © 2016</span>
    <span class="mark">Clinician Supply Circle</span>
  </footer>
</div>
</body>
</html>
```